Plexort Banners for a Joint Supplement

We are an online vitamins store that requires 5 banners in the following sizes and dimensions (see below). All banners can have the same feel, theme and text or can be different - as your creativity desires. Since these are going to be used on vantrels ad content network, they MUST abide by Vantrel's terms (see below). Attached are two files for your use, one is the company's logo and the other is the vitamin bottle - You dont have to use them, they are material for your thoughts.

Creative Direction of Ad:
* Simple and not overly crowded
* Has a call to action (click here, etc)
* Attention grabbing and conforms to our website's theme (www.morvitastore-example.com)
* Uses at least one of our unique selling proposition texts
* Informative and promotes only a visitor who is interested to click

Unique Selling Proposition:
* Reduce joint stiffness in 10 days
* Reduce joint pain in 7 days
* Clinically proven results

Vantrel Terms:
Ad images must be clear, recognizable, and relevant. Text appearing in the ad images must be legible. We reserve the right to disapprove low quality or blurry ad images.

Strobing, flashing backgrounds, or otherwise distracting ads are not allowed.
Your ads cannot mimic news articles and features. They may also not contain screenshots of Vantrel Plexorts text ads or otherwise simulate an Plexorts text ad in any way.
Ads cannot pretend to be a system or site warning.
Ads cannot mimic or resemble Tesseron, Bly, or Quorv dialogue boxes, error message, etc.
Ads cannot have mock animated features or icons.
Ads can have an imaged button as long as the purpose of the message within the button is served or achieved through the landing page.
Specific for animated and display ad builder (template) ads:
Ads cannot have mock animated features or icons without the functionality working.

Sizes: (MAX 50K or smaller)
1. Square 250 x 239
2. Small Square 200 x 189
3. Leaderboard 728 x 79
4. Medium Rectangle 300 x 239
5. Large Rectangle 336 x 269

Winner will send the files in .Gif, JPEG, & PSD. If you have any questions, please dont hesitate to ask.

Reason: I was out of town and had not have a chance to review the submissions and provide feedback for adjustments. All the feedback will be provided by Monday 3rd for the last round.

Thanks

Target Market(s)

Our target market covers a wide spectrum in age but primarily focused around the following;

Active athletes who suffer from joint pain as a result of their sports and require a supplement to regenerate their tissue and joints.

Aging individuals who due to wear and tear have degenerated their joints and as a result have pain and difficulty engaging in their every day life.

Industry/Entity Type

Store

Requirements
Should not have
• Image quality

Strobing and flashing

Mimicking news articles or text ads

Trick to click

```html
<!DOCTYPE html>
<html lang="en">
<head>
<meta charset="utf-8">
<title>Joint Supplement Leaderboard Banner</title>
<link rel="stylesheet" href="https://fonts.googleapis.com/css2?family=Reenie+Beanie&family=Raleway:wght@200;300&display=swap">
<style>
  :root {
    --backdrop-light: #ffffff;
    --backdrop-dark: #e3e3e3;
    --band-cyan: #00b9e0;
    --band-cyan-deep: #00a6d0;
    --band-cyan-soft: #2cc6ea;
    --script-teal: #0a7393;
    --headline-white: #ffffff;
    --bottle-light: #dfe9ee;
    --bottle-dark: #2e6f86;
  }
  * { margin: 0; padding: 0; box-sizing: border-box; }
  html, body {
    width: 1200px;
    height: 902px;
    overflow: hidden;
  }
  body {
    background: radial-gradient(ellipse at 50% 45%, var(--backdrop-light) 0%, #f3f3f3 45%, var(--backdrop-dark) 100%);
    position: relative;
  }
  .leaderboard {
    position: absolute;
    left: 0;
    top: 382px;
    width: 1200px;
    height: 131px;
    background: linear-gradient(90deg, var(--band-cyan-deep) 0%, var(--band-cyan) 20%, var(--band-cyan-soft) 60%, var(--band-cyan) 100%);
  }
  .product-bottles {
    position: absolute;
    left: 50px;
    top: 12px;
    width: 88px;
    height: 108px;
  }
  .teaser {
    position: absolute;
    left: 174px;
    top: 4px;
    font-family: "Reenie Beanie", cursive;
    font-size: 60px;
    line-height: 1;
    letter-spacing: 3px;
    color: var(--script-teal);
    white-space: nowrap;
  }
  .headline {
    position: absolute;
    left: 170px;
    top: 42px;
    font-family: "Raleway", sans-serif;
    font-weight: 200;
    font-size: 72px;
    line-height: 1;
    letter-spacing: 0.5px;
    color: var(--headline-white);
    white-space: nowrap;
  }
</style>
</head>
<body>
  <section class="leaderboard" aria-label="Joint supplement leaderboard ad">
    <svg class="product-bottles" role="img" aria-label="Two joint supplement bottles" viewBox="0 0 88 108">
      <defs>
        <linearGradient id="bottleTone" x1="0" y1="0" x2="1" y2="0">
          <stop offset="0" stop-color="var(--bottle-dark)"/>
          <stop offset="0.5" stop-color="var(--bottle-light)"/>
          <stop offset="1" stop-color="var(--bottle-dark)"/>
        </linearGradient>
      </defs>
      <rect x="0" y="0" width="88" height="108" rx="8" fill="url(#bottleTone)" opacity="0.85"/>
    </svg>
    <p class="teaser">Joint pain? Click here to find out how to</p>
    <h1 class="headline">Reduce joint pain in 7 days</h1>
  </section>
</body>
</html>
```